Corporate Business card, Letter head, & Envelope
CorvaneLG
Professional
Nadia Perrow
CEO
5827 Fenwillow Dr, Suite 408
Brennholt, Ohio 44917
nadiap@corvaneloftsgroup.example
www.corvaneloftsgroup.example
We are a corporate travel management and not a leisure company, so we need to stay professional

```html
<!DOCTYPE html>
<html lang="en">
<head>
<meta charset="utf-8">
<title>CorvaneLG Business Card</title>
<link href="https://fonts.googleapis.com/css2?family=Michroma&family=Montserrat:wght@400;500;600&display=swap" rel="stylesheet">
<style>
  :root {
    --page-bg: #e4e6ea;
    --card-white: #ffffff;
    --brand-blue: #2a3f96;
    --brand-blue-light: #4f7fd0;
    --brand-blue-deep: #1c2a73;
    --accent-orange: #f29a1f;
    --accent-gold: #f7c04a;
    --text-grey: #8a8f99;
    --text-white: #ffffff;
    --faint-blue: #c9d5ee;
  }
  * { margin: 0; padding: 0; box-sizing: border-box; }
  html, body { width: 1200px; height: 980px; overflow: hidden; }
  body {
    background: var(--page-bg);
    font-family: "Montserrat", Arial, sans-serif;
    display: flex;
    align-items: center;
    justify-content: center;
    gap: 40px;
  }
  .card {
    position: relative;
    width: 540px;
    height: 309px;
    background: var(--card-white);
    border-radius: 16px;
    overflow: hidden;
    box-shadow: 0 6px 18px rgba(30, 40, 80, 0.18);
  }
  .card-wave { position: absolute; inset: 0; width: 100%; height: 100%; }

  .contact-list {
    position: absolute;
    left: 22px;
    top: 150px;
    list-style: none;
    color: var(--text-white);
    font-size: 8.5px;
    font-weight: 500;
    letter-spacing: 0.3px;
  }
  .contact-list li { display: flex; align-items: center; gap: 6px; height: 13px; white-space: nowrap; }
  .contact-icon {
    width: 9px; height: 9px; border-radius: 50%;
    background: var(--text-white);
    display: inline-flex; align-items: center; justify-content: center;
    flex-shrink: 0;
  }
  .contact-icon svg { width: 7px; height: 7px; }

  .brand {
    position: absolute;
    left: 200px;
    top: 60px;
    display: flex;
    align-items: center;
    gap: 12px;
  }
  .brand-mark {
    width: 46px; height: 46px; border-radius: 50%;
    background: var(--brand-blue);
    flex-shrink: 0;
  }
  .brand-name {
    font-family: "Michroma", "Arial Black", sans-serif;
    font-size: 22px;
    color: var(--brand-blue);
    letter-spacing: 1px;
  }
  .brand-tagline {
    font-family: "Michroma", "Arial Black", sans-serif;
    font-size: 7.5px;
    color: var(--accent-orange);
    letter-spacing: 1.2px;
    margin-top: 4px;
  }

  .person {
    position: absolute;
    right: 26px;
    bottom: 22px;
    text-align: right;
    color: var(--text-white);
    font-family: "Michroma", "Arial Black", sans-serif;
    font-size: 11px;
    letter-spacing: 1.5px;
    line-height: 1.6;
  }
  .person-role { font-size: 9px; }

  .back-website {
    position: absolute;
    left: 26px;
    top: 26px;
    font-family: "Michroma", "Arial Black", sans-serif;
    font-size: 10px;
    color: var(--text-grey);
    letter-spacing: 1.5px;
  }
  .back-brand {
    position: absolute;
    right: 36px;
    top: 112px;
    display: flex;
    align-items: center;
    gap: 14px;
    opacity: 0.55;
  }
  .back-brand .brand-mark { width: 84px; height: 84px; background: var(--faint-blue); }
  .back-brand .brand-name { color: var(--faint-blue); font-size: 20px; }
</style>
</head>
<body>

  <section class="card card-front">
    <svg class="card-wave" viewBox="0 0 540 309" preserveAspectRatio="none" aria-hidden="true">
      <defs>
        <radialGradient id="blueSweep" cx="0.45" cy="0.75" r="0.75">
          <stop offset="0" stop-color="#5b8fde"/>
          <stop offset="0.55" stop-color="#2f4aa3"/>
          <stop offset="1" stop-color="#1c2a73"/>
        </radialGradient>
        <linearGradient id="orangeLine" x1="0" x2="1">
          <stop offset="0" stop-color="#f7c04a"/>
          <stop offset="0.5" stop-color="#f29a1f"/>
          <stop offset="1" stop-color="#f7c04a"/>
        </linearGradient>
      </defs>
      <path d="M0,124 C120,120 230,160 330,176 C420,192 490,175 540,150 L540,309 L0,309 Z" fill="url(#blueSweep)"/>
      <path d="M0,116 C120,112 230,152 330,168 C420,184 490,167 540,142" fill="none" stroke="url(#orangeLine)" stroke-width="4"/>
      <path d="M0,110 C120,106 230,146 330,162 C420,178 490,161 540,136" fill="none" stroke="var(--brand-blue-light)" stroke-width="1.2" opacity="0.6"/>
    </svg>

    <div class="brand">
      <div class="brand-mark"></div>
      <div>
        <div class="brand-name">CorvaneLG</div>
        <div class="brand-tagline">TRAVEL MANAGEMENT COMPANY</div>
      </div>
    </div>

    <ul class="contact-list">
      <li><span class="contact-icon"><svg viewBox="0 0 10 10"><path d="M5 1a3 3 0 0 1 3 3c0 2-3 5-3 5S2 6 2 4a3 3 0 0 1 3-3z" fill="#2a3f96"/></svg></span>5827 Fenwillow Dr, Suite 408</li>
      <li><span class="contact-icon"><svg viewBox="0 0 10 10"><path d="M5 1a3 3 0 0 1 3 3c0 2-3 5-3 5S2 6 2 4a3 3 0 0 1 3-3z" fill="#2a3f96"/></svg></span>Brennholt, Ohio 44917</li>
      <li><span class="contact-icon"><svg viewBox="0 0 10 10"><path d="M2 2h2l1 2-1 1a5 5 0 0 0 2 2l1-1 2 1v2C5 9 1 5 2 2z" fill="#2a3f96"/></svg></span>972-555-0143</li>
      <li><span class="contact-icon"><svg viewBox="0 0 10 10"><path d="M2 2h2l1 2-1 1a5 5 0 0 0 2 2l1-1 2 1v2C5 9 1 5 2 2z" fill="#2a3f96"/></svg></span>972-555-0187</li>
      <li><span class="contact-icon"><svg viewBox="0 0 10 10"><circle cx="5" cy="5" r="2.5" fill="#2a3f96"/></svg></span>kiwlen42</li>
      <li><span class="contact-icon"><svg viewBox="0 0 10 10"><circle cx="5" cy="5" r="2.5" fill="#2a3f96"/></svg></span>Corvane_Lofts</li>
      <li><span class="contact-icon"><svg viewBox="0 0 10 10"><rect x="1.5" y="3" width="7" height="4.5" fill="none" stroke="#2a3f96" stroke-width="1"/><path d="M1.5 3l3.5 2.5L8.5 3" fill="none" stroke="#2a3f96" stroke-width="1"/></svg></span>nadiap@corvaneloftsgroup.example</li>
      <li><span class="contact-icon"><svg viewBox="0 0 10 10"><circle cx="5" cy="5" r="3" fill="none" stroke="#2a3f96" stroke-width="1"/><path d="M2 5h6M5 2v6" stroke="#2a3f96" stroke-width="0.8"/></svg></span>www.corvaneloftsgroup.example</li>
    </ul>

    <div class="person">
      <div class="person-name">NADIA PERROW</div>
      <div class="person-role">CEO</div>
    </div>
  </section>

  <section class="card card-back">
    <div class="back-website">www.corvaneloftsgroup.example</div>
    <div class="back-brand">
      <div class="brand-mark"></div>
      <div class="brand-name">CorvaneLG</div>
    </div>
  </section>

</body>
</html>
```